New one page Homepage with registration and log in form

Hi designers!

We need a new homepage and made a skitch of how it should be.

Can you give some of your design ideas and work it out so that it actually looks great?

Its just one page, for convertion reasons.

The logo doesnt have to be changed.

It would be cool to center the logo but not sure how design technically correct that is.

The social icons can be left out.

If you could give a few mockups than we can choose the best one.

I added one screenshot sketch of the homepage.

And 2 screenshots of what the system looks like on the inside, just so you get an idea.

Thanks

Target Market(s)

Vacation rental owners who want to increase their bookings by connecting with other VR owners and managers, or by having their own booking team for a small fee.

Industry/Entity Type

Social

Number of Pages Required

1 page

Requirements
Must have
• Use your imagination please
Nice to have
• Use your imagination
• It will be a one page design so we need to impress :)
• Keep it compact, maybe a web 3.0 flat design, etc
Should not have
• Other pages.

```html
<!DOCTYPE html>
<html lang="en">
<head>
<meta charset="utf-8">
<title>StayNest – The First Social Booking Network</title>
<link rel="stylesheet" href="https://fonts.googleapis.com/css2?family=Open+Sans:wght@400;600;700&display=swap">
<style>
  :root {
    --orange: #ff7305;
    --ink: #111111;
    --blue-title: #1d5aa8;
    --brand-blue: #0b4c9c;
    --green: #a8c935;
    --panel: rgba(255, 250, 244, 0.86);
    --field-border: #9a9a9a;
    --alert-red: #e0301e;
    --white: #ffffff;
    --photo-light: #efe3d2;
    --photo-mid: #d9bc98;
    --photo-dark: #a98660;
  }
  * { box-sizing: border-box; margin: 0; padding: 0; }
  html, body { width: 1200px; height: 665px; overflow: hidden; }
  body { font-family: "Open Sans", Arial, sans-serif; color: var(--ink); }

  .page { position: relative; width: 1200px; height: 665px; overflow: hidden; }

  .backdrop {
    position: absolute; inset: 0;
    background:
      radial-gradient(ellipse at 20% 30%, rgba(255,255,255,0.55), transparent 55%),
      radial-gradient(ellipse at 85% 40%, rgba(255,255,255,0.6), transparent 50%),
      linear-gradient(180deg, var(--photo-light) 0%, var(--photo-mid) 60%, var(--photo-dark) 100%);
  }
  .header-photo {
    position: absolute; left: 0; top: 0; width: 1200px; height: 106px;
    background: linear-gradient(90deg, #b89a78 0%, #e8dccb 35%, #d8c3a8 55%, #f3efe8 80%, #e4dbcd 100%);
  }

  .brand { position: absolute; left: 268px; top: 18px; }
  .brand-name {
    display: flex; align-items: center; gap: 8px;
    font-size: 30px; font-weight: 700; color: var(--brand-blue); line-height: 1;
  }
  .brand-mark { width: 18px; height: 18px; border-radius: 50%; background: var(--orange); }
  .brand-tagline { margin-top: 10px; font-size: 14px; font-weight: 700; color: var(--brand-blue); }

  .top-bar { position: absolute; left: 0; top: 106px; width: 1200px; height: 29px; background: var(--orange); }
  .lock-icon { position: absolute; left: 967px; top: 4px; }

  .headline {
    position: absolute; left: 0; width: 1212px; top: 138px; text-align: center;
    font-size: 43px; font-weight: 600; letter-spacing: 1.4px;
  }

  .intro {
    position: absolute; left: 234px; top: 203px;
    font-size: 14.5px; line-height: 17.3px; letter-spacing: 0.6px; font-weight: 600;
  }
  .intro-line { display: block; white-space: nowrap; }

  .video {
    position: absolute; left: 654px; top: 206px; width: 330px; height: 184px;
    background: #000; display: flex; align-items: center; justify-content: center;
  }

  .account-panel {
    position: absolute; left: 234px; top: 431px; width: 731px; height: 215px;
    background: var(--panel); border-radius: 10px;
  }
  .divider { position: absolute; left: 345px; top: 12px; width: 1px; height: 196px; background: var(--orange); }
  .panel-title { font-size: 16px; font-weight: 600; color: var(--blue-title); text-align: center; }

  .login { position: absolute; left: 0; top: 10px; width: 300px; }
  .login .panel-title { position: absolute; left: 0; width: 300px; }
  .pill-field {
    position: absolute; left: 35px; width: 235px; height: 21px; border-radius: 11px;
    background: var(--green); color: var(--white); font-size: 12.5px;
    text-align: center; line-height: 21px;
  }
  .remember { position: absolute; left: 38px; top: 95px; display: flex; align-items: center; gap: 7px; font-size: 9.5px; }
  .remember-box { width: 9px; height: 9px; border: 1px solid #333; background: var(--white); }
  .social-signin {
    position: absolute; left: 56px; top: 117px; width: 202px; height: 44px;
    background: var(--brand-blue); border: 1px solid #062c5c; color: var(--white);
    display: flex; align-items: center; gap: 12px; padding-left: 16px; font-size: 13.5px;
  }
  .social-mark { width: 12px; height: 12px; background: var(--white); }
  .forgot { position: absolute; left: 0; width: 305px; top: 177px; text-align: center; font-size: 10px; color: var(--alert-red); }

  .register { position: absolute; left: 376px; top: 10px; width: 326px; }
  .register .panel-title { width: 302px; }
  .register-sub { width: 302px; text-align: center; font-size: 10px; margin-top: 1px; }
  .text-field {
    position: absolute; height: 16px; background: var(--white);
    border: 1px solid var(--field-border); font-size: 9.5px; line-height: 14px; padding-left: 9px;
  }
  .submit {
    position: absolute; left: 96px; top: 155px; width: 148px; height: 32px;
    background: var(--orange); border-radius: 10px; color: var(--white);
    font-size: 16px; font-weight: 700; text-align: center; line-height: 32px;
  }
</style>
</head>
<body>
<main class="page">
  <div class="backdrop" role="img" aria-label="Soft blurred photo of a garden terrace with a wooden railing in warm light"></div>
  <div class="header-photo" role="img" aria-label="Photo of an older couple seen from behind looking at a stately house"></div>

  <div class="brand">
    <div class="brand-name"><span class="brand-mark"></span>StayNest</div>
    <div class="brand-tagline">stays shared, bookings grown</div>
  </div>

  <div class="top-bar">
    <svg class="lock-icon" width="16" height="20" viewBox="0 0 16 20" aria-label="Secure">
      <path d="M4 9V6a4 4 0 0 1 8 0v3" fill="none" stroke="#000" stroke-width="2.2"/>
      <rect x="1" y="9" width="14" height="10" rx="1" fill="#000"/>
      <rect x="7" y="12" width="2" height="4" fill="var(--orange)"/>
    </svg>
  </div>

  <h1 class="headline">The First Social Booking Network</h1>

  <p class="intro">
    <span class="intro-line">Lorem ipsum dolor sit amet, consectetuer</span>
    <span class="intro-line">adipiscing elit, sed diam nonummy nibh euismod</span>
    <span class="intro-line">tincidunt ut laoreet dolore magna aliquam erat</span>
    <span class="intro-line">volutpat.</span>
    <span class="intro-line">Ut wisi enim ad minim veniam, quis</span>
    <span class="intro-line">nostrud exerci tation ullamcorper suscipit</span>
    <span class="intro-line">lobortis nisl ut aliquip ex ea commodo</span>
    <span class="intro-line">consequat.</span>
    <span class="intro-line">Duis autem vel eum iriure dolor in hendrerit in</span>
    <span class="intro-line">vulputate velit esse molestie consequat, vel illum</span>
    <span class="intro-line">dolore eu feugiat nulla facilisis at vero eros et</span>
  </p>

  <div class="video">
    <svg width="46" height="54" viewBox="0 0 46 54" aria-label="Play video">
      <polygon points="0,0 46,27 0,54" fill="var(--orange)"/>
    </svg>
  </div>

  <section class="account-panel">
    <div class="login">
      <h2 class="panel-title">Login to your account</h2>
      <div class="pill-field" style="top:37px">username or email address</div>
      <div class="pill-field" style="top:68px">password</div>
      <div class="remember"><span class="remember-box"></span>Would you like us to remember you?</div>
      <div class="social-signin"><span class="social-mark"></span>Sign in with Linkbook</div>
      <div class="forgot">Forgot username/password</div>
    </div>

    <div class="divider"></div>

    <div class="register">
      <h2 class="panel-title">Don’t have an account?</h2>
      <p class="register-sub">Register now to join the Free Booking Network!</p>
      <div class="text-field" style="left:0;top:46px;width:163px">First Name</div>
      <div class="text-field" style="left:168px;top:46px;width:158px">Last Name</div>
      <div class="text-field" style="left:0;top:66px;width:326px">Password</div>
      <div class="text-field" style="left:0;top:87px;width:326px">user@email.com</div>
      <div class="text-field" style="left:0;top:109px;width:326px">Set your contact number, Example : +1234567890</div>
      <div class="text-field" style="left:0;top:130px;width:326px">Whats your reason for joining?</div>
      <div class="submit">Submit</div>
    </div>
  </section>
</main>
</body>
</html>
```